Vivaform - Fitness Coach. Needs a Business Card Design that I can also use for other advertising

Established 2012, I have finished the QPLB National Certificate in Fitness & Personal Training. Harrowgate First Aid Certificate. I have the Auckland 800m track records for MW45. I also came 1st at the 2012 Pacifica Games in 800 & 1500m. I am passionate about health & fitness and would like to help people reach their health & fitness goals. I also take health & fitness weekends. Main interests - Running, Weight Training, Yoga & Aqua Jogging. I like strength/power, but am femine.

Target Market(s)

Male or Female 18 and over that wants to improve their health & fitness

Industry/Entity Type

Advertising

Requirements
Must have
• my name: Lorissa K Dunmore contact details: lori@brightpath.co.nz mobile - 021 579318 URL name: facebook.com/lorissaKdunmore - VivaForm
Photo of Me

```html
<!DOCTYPE html>
<html lang="en">
<head>
<meta charset="utf-8">
<title>VivaForm – Business Card</title>
<link href="https://fonts.googleapis.com/css2?family=Domine:wght@700&family=PT+Sans:wght@400;700&display=swap" rel="stylesheet">
<style>
  :root {
    --page: #ededeb;
    --card: #ffffff;
    --teal: #00998a;
    --teal-light: #8fd6cf;
    --red: #d5404f;
    --leaf-dark: #2f4a1f;
    --leaf-mid: #5f8a35;
    --leaf-light: #9cbf5a;
    --ink: #1f2b2a;
  }
  html, body {
    margin: 0;
    width: 1200px;
    height: 900px;
    overflow: hidden;
    background: var(--page);
  }
  .stage {
    position: relative;
    width: 1200px;
    height: 900px;
  }
  .card {
    position: absolute;
    top: 74px;
    width: 422px;
    height: 736px;
    background: var(--card);
    overflow: hidden;
  }
  .card--front { left: 138px; }
  .card--back  { left: 641px; }
  .card svg { display: block; width: 422px; height: 736px; }
  .brand-name {
    font-family: "Domine", Georgia, serif;
    font-weight: 700;
    font-size: 96px;
    fill: #ffffff;
  }
  .holder-name {
    font-family: "PT Sans", Arial, sans-serif;
    font-weight: 700;
    font-size: 60px;
    fill: var(--teal);
  }
  .contact-text {
    font-family: "PT Sans", Arial, sans-serif;
    font-size: 20px;
    fill: var(--ink);
  }
  .contact-icon { fill: none; stroke: var(--red); stroke-width: 2; }
  .contact-icon--solid { fill: var(--red); stroke: none; }
</style>
</head>
<body>
<main class="stage">

  <!-- Front of card -->
  <section class="card card--front">
    <svg viewBox="0 0 422 736" xmlns="http://www.w3.org/2000/svg">
      <defs>
        <linearGradient id="hedge" x1="0" y1="0" x2="0.3" y2="1">
          <stop offset="0" stop-color="var(--leaf-mid)"/>
          <stop offset="0.45" stop-color="var(--leaf-dark)"/>
          <stop offset="1" stop-color="var(--leaf-light)"/>
        </linearGradient>
      </defs>
      <rect class="portrait" x="0" y="0" width="422" height="600" fill="url(#hedge)"
            role="img" aria-label="Photo of the coach leaping in front of a green hedge"/>
      <path class="portrait-frame" fill="#ffffff" fill-opacity="0.45" fill-rule="evenodd"
            d="M0 0 H422 V600 H0 Z M-59 297 A270 262 0 1 0 481 297 A270 262 0 1 0 -59 297 Z"/>
      <path class="wave wave--red" fill="var(--red)"
            d="M0 532 Q200 600 422 526 V736 H0 Z"/>
      <path class="wave wave--teal" fill="var(--teal)"
            d="M0 568 Q220 620 422 538 V736 H0 Z"/>
      <text class="brand-name" x="211" y="698" text-anchor="middle" textLength="370" lengthAdjust="spacingAndGlyphs">VivaForm</text>
    </svg>
  </section>

  <!-- Back of card -->
  <section class="card card--back">
    <svg viewBox="0 0 422 736" xmlns="http://www.w3.org/2000/svg">
      <text class="holder-name" transform="translate(44 58) rotate(90)">Lorissa K Dunmore</text>

      <g class="contact contact--phone">
        <rect class="contact-icon" x="120" y="521" width="11" height="18" rx="2"/>
        <line class="contact-icon" x1="124" y1="535" x2="127" y2="535"/>
        <text class="contact-text" x="147" y="537">021 579318</text>
      </g>
      <g class="contact contact--email">
        <rect class="contact-icon" x="117" y="556" width="17" height="12"/>
        <polyline class="contact-icon" points="117,556 125.5,563 134,556"/>
        <text class="contact-text" x="147" y="566">lori@brightpath.co.nz</text>
      </g>
      <g class="contact contact--social">
        <rect class="contact-icon--solid" x="118" y="579" width="15" height="15"/>
        <text class="contact-text" x="147" y="594">lorissaKdunmore</text>
      </g>

      <path class="wave wave--light" fill="var(--teal-light)"
            d="M0 642 Q230 670 422 601 V736 H0 Z"/>
      <path class="wave wave--red" fill="var(--red)"
            d="M0 644 Q230 690 422 640 V736 H0 Z"/>
      <path class="wave wave--teal" fill="var(--teal)"
            d="M0 688 Q230 700 422 661 V736 H0 Z"/>
    </svg>
  </section>

</main>
</body>
</html>
```